Pro-life non-profit needs a dynamic poster design for their Christmas Gala.

We need a poster design which plays off the name of the event, The Winter Lantern. The Winter Lantern, of course is the Baby Jesus. Our cause supports unborn children in Iowa. The gala will include a concert of popular Christmas music sung by top soloists backed by an orchestra. An original commissioned song, The Winter Lantern, will be premiered. Purple and gold colors immediately come to mind, but a designer should not feel constrained on colors. We need an editable design w/fonts. Photoshop w/layers or Illustrator files are good.

```html
<!DOCTYPE html>
<html lang="en">
<head>
<meta charset="utf-8">
<title>The Winter Lantern – A Pro-Life Christmas Gala</title>
<link rel="stylesheet" href="https://fonts.googleapis.com/css2?family=Cinzel+Decorative:wght@700&family=Work+Sans:wght@600;700&family=Alegreya+SC:wght@500&family=Oswald:wght@500&family=Prata&display=swap">
<style>
  :root {
    --wine-deep: #5a0610;
    --wine: #8e1420;
    --wine-bright: #a81c2a;
    --gold: #c9953f;
    --gold-light: #e2b560;
    --cream: #fbf1e0;
    --pearl: #eeeaf0;
    --ink-red: #7a0f18;
    --ink: #1d1416;
  }
  * { margin: 0; padding: 0; box-sizing: border-box; }
  html, body { width: 900px; height: 1200px; overflow: hidden; background: var(--wine-deep); }
  .poster { position: relative; width: 900px; height: 1200px; overflow: hidden; }
  .poster-art {
    position: absolute; inset: 0;
    background:
      radial-gradient(ellipse 55% 45% at 52% 40%, var(--wine-bright) 0%, rgba(168,28,42,0) 70%),
      radial-gradient(ellipse 80% 70% at 50% 50%, var(--wine) 0%, var(--wine-deep) 100%);
  }
  .frame, .bottom-band { position: absolute; inset: 0; }
  .centered { position: absolute; left: 0; width: 100%; text-align: center; white-space: nowrap; }
  .title-the {
    top: 140px; font-family: "Cinzel Decorative", serif; font-weight: 700;
    font-size: 150px; line-height: 1; color: var(--gold);
  }
  .title-main {
    top: 362px; font-family: "Cinzel Decorative", serif; font-weight: 700;
    font-size: 76px; line-height: 1; color: var(--gold); letter-spacing: -1px;
  }
  .subtitle {
    top: 510px; font-family: "Work Sans", sans-serif; font-weight: 700;
    font-size: 39px; line-height: 48px; color: var(--cream); letter-spacing: 0.5px;
  }
  .details {
    position: absolute; font-family: "Alegreya SC", serif; font-weight: 500;
    font-size: 19px; line-height: 24px; color: var(--cream); text-align: center; white-space: nowrap;
  }
  .details-when { left: 50px; width: 370px; top: 632px; }
  .details-price { left: 470px; width: 370px; top: 646px; }
  .speaker {
    top: 743px; font-family: "Work Sans", sans-serif; font-weight: 700;
    font-size: 20px; line-height: 28px; color: var(--cream);
  }
  .speaker-label { color: var(--gold); font-size: 24px; margin-right: 14px; letter-spacing: 0.5px; }
  .seating {
    top: 814px; font-family: "Oswald", sans-serif; font-weight: 500;
    font-size: 33px; line-height: 44px; color: var(--cream); letter-spacing: 0.5px;
  }
  .order {
    top: 877px; font-family: "Work Sans", sans-serif; font-weight: 600;
    font-size: 19px; line-height: 26px; color: var(--cream);
  }
  .contacts {
    top: 905px; font-family: "Work Sans", sans-serif; font-weight: 600;
    font-size: 18px; line-height: 26px; color: var(--cream);
  }
  .icon { display: inline-block; vertical-align: -3px; margin: 0 6px 0 10px; }
  .presenter {
    position: absolute; left: 180px; top: 1030px; width: 190px; text-align: center;
    font-family: "Prata", serif; color: var(--ink);
  }
  .presenter-name { font-size: 22px; line-height: 1.3; }
  .presenter-tag { font-size: 24px; letter-spacing: 2px; margin-top: 14px; }
  .presenter-rule { position: absolute; left: 382px; top: 1040px; width: 2px; height: 78px; background: var(--ink-red); }
  .banquet {
    position: absolute; left: 395px; top: 1045px; width: 330px; text-align: center;
    font-family: "Prata", serif; font-size: 29px; line-height: 38px; color: var(--ink-red);
  }
</style>
</head>
<body>
<main class="poster">
  <div class="poster-art" role="img" aria-label="Deep red painted background artwork with soft warm glow and festive sparkles"></div>

  <svg class="frame" width="900" height="1200" viewBox="0 0 900 1200" aria-hidden="true">
    <rect x="20" y="22" width="860" height="1158" fill="none" stroke="var(--gold)" stroke-width="3"/>
    <rect x="28" y="30" width="844" height="1142" fill="none" stroke="var(--gold)" stroke-width="1.2"/>
    <line x1="48" y1="298" x2="285" y2="298" stroke="var(--gold)" stroke-width="2"/>
    <line x1="615" y1="298" x2="852" y2="298" stroke="var(--gold)" stroke-width="2"/>
    <line x1="52" y1="578" x2="848" y2="578" stroke="var(--gold)" stroke-width="1.5"/>
    <path d="M400 578 Q450 556 500 578 Q450 600 400 578 Z" fill="var(--gold)"/>
  </svg>

  <div class="centered title-the">THE</div>
  <div class="centered title-main">Winter Lantern</div>
  <div class="centered subtitle">A PRO-LIFE CHRISTMAS GALA</div>

  <div class="details details-when">
    Saturday, November 21st, 2020<br>
    Doors open at 5:30pm<br>
    Maple Hall Center, W. Des Moines, IA
  </div>
  <div class="details details-price">
    $60 Person · $500 Table of Ten<br>
    Cocktails · Dinner · Christmas Concert
  </div>

  <div class="centered speaker"><span class="speaker-label">SPECIAL GUEST SPEAKER:</span>BISHOP THOMAS RANDELL</div>
  <div class="centered seating">SEATING LIMITED · RESERVATIONS NEEDED</div>
  <div class="centered order">ORDER TICKETS ONLINE:
    <svg class="icon" width="18" height="18" viewBox="0 0 18 18" aria-hidden="true"><circle cx="9" cy="9" r="7.5" fill="none" stroke="var(--gold)" stroke-width="1.6"/><ellipse cx="9" cy="9" rx="3.3" ry="7.5" fill="none" stroke="var(--gold)" stroke-width="1.3"/><line x1="1.5" y1="9" x2="16.5" y2="9" stroke="var(--gold)" stroke-width="1.3"/></svg>www.HeartlandForLife.org
  </div>
  <div class="centered contacts">
    <svg class="icon" width="17" height="17" viewBox="0 0 24 24" aria-hidden="true"><path d="M6.6 10.8c1.4 2.8 3.8 5.1 6.6 6.6l2.2-2.2c.3-.3.7-.4 1-.2 1.1.4 2.3.6 3.6.6.6 0 1 .4 1 1V20c0 .6-.4 1-1 1C10.6 21 3 13.4 3 4c0-.6.4-1 1-1h3.5c.6 0 1 .4 1 1 0 1.3.2 2.5.6 3.6.1.3 0 .7-.2 1z" fill="var(--gold)"/></svg>515-555-0142
    <svg class="icon" width="18" height="14" viewBox="0 0 18 14" aria-hidden="true"><rect x="0" y="0" width="18" height="14" rx="1.5" fill="var(--gold)"/><path d="M1 1.5 9 8 17 1.5" fill="none" stroke="var(--wine)" stroke-width="1.6"/></svg>events@heartlandforlife.org
  </div>

  <svg class="bottom-band" width="900" height="1200" viewBox="0 0 900 1200" aria-hidden="true">
    <defs>
      <radialGradient id="pearlGlow" cx="50%" cy="55%" r="70%">
        <stop offset="0" stop-color="#ffffff"/>
        <stop offset="1" stop-color="var(--pearl)"/>
      </radialGradient>
    </defs>
    <path d="M0 990 Q220 940 420 965 Q450 970 450 980 Q450 970 480 965 Q680 940 900 990 L900 1200 L0 1200 Z" fill="var(--gold)"/>
    <path d="M0 1002 Q220 952 420 977 Q450 982 450 992 Q450 982 480 977 Q680 952 900 1002 L900 1200 L0 1200 Z" fill="url(#pearlGlow)"/>
    <path d="M20 1020 L20 1180 L880 1180 L880 1020" fill="none" stroke="var(--gold)" stroke-width="3"/>
    <path d="M28 1024 L28 1172 L872 1172 L872 1024" fill="none" stroke="var(--gold)" stroke-width="1.2"/>
  </svg>

  <div class="presenter">
    <div class="presenter-name">Heartland for Life</div>
    <div class="presenter-tag">Presents</div>
  </div>
  <div class="presenter-rule"></div>
  <div class="banquet">The Tenth Annual<br>Fundraising Banquet</div>
</main>
</body>
</html>
```